wooden jewelry - pearl necklaces

I sell wooden jeweler (rings and pearls) on markets, and so on. I also opened my business as a carpenter. The rings and a combination of wood and metal. The wood is special wood, not very common on Europe. I paint the rings afterwards. You can see some of the pictures on the pictures I uploaded. The pearls are made of the same kind of wood and colored in all kinds of colors. They are then assembled to bracelets. The jewelry is very individual and looks really cool and all kinds of people.

Target Market(s)

Young urban alternative with a sense of individuality

Contact Information for Business Card

Front:

Text:

„Kugelwerk“ (big)
„Malte Oswitz“ (smaler)

Back
„Holzschmuck
Herstellung von individuellem Holz- und Modeschmuck

Malte Oswitz
Tel: 015239460518
Lindgarbweg 9
83127 Burghausen

malteoswitz@postfeld.de“

Font styles to use
Sans Serif

Requirements
Nice to have
• Nice to see a camel thorn tree on the background, this is a special wood and some of the rings are made out of this wood.

```html
<!DOCTYPE html>
<html lang="de">
<head>
<meta charset="utf-8">
<title>Kugelwerk – Visitenkarte</title>
<link href="https://fonts.googleapis.com/css2?family=Bebas+Neue&family=Work+Sans:wght@400;500&display=swap" rel="stylesheet">
<style>
  :root {
    --page-bg: #dedede;
    --bead-dark: #1c120d;
    --bead-brown: #4a2a1a;
    --bead-amber: #7a5526;
    --bead-red: #5e1a1c;
    --band: rgba(20, 12, 8, 0.5);
    --text-light: #ffffff;
    --text-soft: #ece6df;
  }
  * { margin: 0; padding: 0; box-sizing: border-box; }
  html, body {
    width: 1200px;
    height: 897px;
    overflow: hidden;
    background: var(--page-bg);
  }
  .canvas {
    position: relative;
    width: 1200px;
    height: 897px;
  }
  .card {
    position: absolute;
    left: 326px;
    width: 543px;
    height: 311px;
    overflow: hidden;
  }
  .card--front { top: 127px; }
  .card--back { top: 474px; }
  .bead-photo {
    position: absolute;
    inset: 0;
    background:
      radial-gradient(circle at 12% 20%, rgba(122, 85, 38, 0.75) 0 9%, transparent 16%),
      radial-gradient(circle at 30% 65%, rgba(94, 26, 28, 0.55) 0 7%, transparent 14%),
      radial-gradient(circle at 55% 35%, rgba(122, 85, 38, 0.6) 0 10%, transparent 18%),
      radial-gradient(circle at 78% 70%, rgba(74, 42, 26, 0.8) 0 9%, transparent 17%),
      radial-gradient(circle at 88% 22%, rgba(122, 85, 38, 0.55) 0 8%, transparent 15%),
      radial-gradient(circle at 45% 85%, rgba(122, 85, 38, 0.5) 0 9%, transparent 16%),
      linear-gradient(135deg, var(--bead-brown), var(--bead-dark) 45%, var(--bead-brown) 70%, var(--bead-dark));
  }
  .info-band {
    position: absolute;
    left: 0;
    right: 0;
    top: 222px;
    height: 70px;
    background: var(--band);
  }
  .brand {
    position: absolute;
    left: 24px;
    top: 229px;
    color: var(--text-light);
  }
  .brand__name {
    font-family: "Bebas Neue", sans-serif;
    font-weight: 400;
    font-size: 34px;
    letter-spacing: 1.8px;
    line-height: 1;
  }
  .brand__person {
    font-family: "Work Sans", sans-serif;
    font-size: 13px;
    margin-top: 3px;
    color: var(--text-soft);
  }
  .contact {
    position: absolute;
    left: 334px;
    top: 231px;
    list-style: none;
    font-family: "Work Sans", sans-serif;
    font-size: 13.5px;
    letter-spacing: 0.6px;
    line-height: 18.5px;
    color: var(--text-light);
  }
  .back-info {
    position: absolute;
    inset: 0;
    display: flex;
    flex-direction: column;
    align-items: center;
    justify-content: center;
    text-align: center;
    color: var(--text-light);
    font-family: "Work Sans", sans-serif;
  }
  .back-info__title {
    font-family: "Bebas Neue", sans-serif;
    font-weight: 400;
    font-size: 30px;
    letter-spacing: 1.6px;
    line-height: 1;
  }
  .back-info__tagline {
    font-size: 12px;
    letter-spacing: 0.4px;
    color: var(--text-soft);
    margin-top: 4px;
  }
  .back-info__details {
    list-style: none;
    margin-top: 14px;
    font-size: 13px;
    letter-spacing: 0.6px;
    line-height: 18px;
  }
  .back-info__url {
    margin-top: 12px;
    font-size: 15px;
    letter-spacing: 1.2px;
  }
</style>
</head>
<body>
<main class="canvas">
  <section class="card card--front">
    <div class="bead-photo" role="img" aria-label="Foto vieler bunter Holzperlen, abgedunkelt"></div>
    <div class="info-band"></div>
    <div class="brand">
      <h1 class="brand__name">Kugelwerk</h1>
      <p class="brand__person">Malte Oswitz</p>
    </div>
    <ul class="contact">
      <li>015239460518</li>
      <li>malteoswitz@postfeld.de</li>
      <li>www.kugelwerkholz.com</li>
    </ul>
  </section>

  <section class="card card--back">
    <div class="bead-photo" role="img" aria-label="Foto vieler bunter Holzperlen, abgedunkelt"></div>
    <div class="back-info">
      <h2 class="back-info__title">Holzschmuck</h2>
      <p class="back-info__tagline">Herstellung von individuellem Holz- und Modeschmuck</p>
      <ul class="back-info__details">
        <li>Malte Oswitz</li>
        <li>Tel: 015239460518</li>
        <li>Lindgarbweg 9</li>
        <li>83127 Burghausen</li>
        <li>malteoswitz@postfeld.de</li>
      </ul>
      <p class="back-info__url">www.kugelwerkholz.com</p>
    </div>
  </section>
</main>
</body>
</html>
```